K&R Flame Guard Supply Inc. needs an updated/new website design

I would like the customer to be able to see who we are, where are are, what we do and areas we cover on the first page. I would like something modern but professional. The other fire safety companies out there have very boring & unappealing websites. I want mine seem like we've got it together and to be above average in comparison. I would like the colors to go with our logo and would like to incorporate somewhere that we have been in business for over 30 years, we are family owned and operated and that we provide service to all of central Florida from Tampa to Titusville and all of Brevard county (we can take out the" all of Brevard county" but keep the " All of Central Florida from Tampa to Titusville" and just add all counties we service to the very bottom too). We are a residential and commercial fire safety equipment company. We do sales, service and installation for fire extinguishers, emergency/exit lighting, kitchen fire suppression systems, fire alarms & fire extinguisher cabinets.I have also attached some pictures that you can use to incorporate any way you would like. Here's our current website (awful I know) to get information from if needed. kandrflameguard.example

Target Market(s)

Restaurants, hotels, vacation rental properties & small businesses. Every business is required to have a fire extinguisher and exit lighting.

Industry/Entity Type

Fire Safety

Number of Pages Required

1 page

Font styles to use
Other font styles liked:
• I'm open to your suggestions

Colors

Designer to choose colors to be used in the design.

Requirements
Must have
• I would like the customer to be able to see who we are, where are are, what we do and areas we cover on the first page. I would like the colors to go with our logo and would like to incorporate somewhere that we have been in business for over 30 years, we are family owned and operated and that we provide service to all of central Florida from Tampa to Titusville and all of Brevard county (we can take out the" all of Brevard county" but keep the " All of Central Florida from Tampa to Titusville" and just add all counties we service to the very bottom too)
Nice to have
• Modern with high quality pictures
• I love the raised logo that I added in the attachments. If you could make the logo look like that in incorporate it as one of the first things you see that would be awesome!
• I would eventually like to have a portfolio of work completed on an additional page.
Should not have
• boring outdated look

```html
<!DOCTYPE html>
<html lang="en">
<head>
<meta charset="utf-8">
<title>K&amp;R Flame Guard Supply Inc.</title>
<link href="https://fonts.googleapis.com/css2?family=Roboto:wght@400;500;700;900&display=swap" rel="stylesheet">
<style>
:root{
  --ink:#1f1f1f;
  --dark:#231f1e;
  --orange:#f15a22;
  --gold:#f7c51a;
  --frame:#f6a01a;
  --grey-bg:#e8e8e8;
  --text-grey:#555;
  --line:#c9c9c9;
  --white:#fff;
}
*{box-sizing:border-box;margin:0;padding:0}
html,body{width:1200px;height:3255px;overflow:hidden}
body{font-family:'Roboto',Arial,sans-serif;color:var(--ink);background:var(--white);position:relative}

.site-header{height:104px;background:var(--dark);display:flex;align-items:center;justify-content:space-between;padding:0 87px}
.brand{display:flex;align-items:center;gap:12px;color:var(--white);font-weight:700;font-size:17px;letter-spacing:.3px}
.brand-mark{width:26px;height:26px;background:var(--orange)}
.main-nav{display:flex;gap:52px}
.main-nav a{color:var(--white);text-decoration:none;font-size:13.5px;font-weight:700;position:relative;padding-bottom:10px}
.main-nav a.active::after{content:"";position:absolute;left:0;right:0;bottom:0;height:3px;background:var(--orange)}

.hero{height:467px;position:relative;background:linear-gradient(100deg,#2b2624 0%,#4a3f3a 40%,#5e4d45 60%,#3a302c 100%)}
.hero-photo{position:absolute;inset:0}
.hero-copy{position:absolute;left:87px;top:158px;width:560px;color:var(--white)}
.hero-copy h1{font-size:30px;font-weight:700;line-height:1.3}
.hero-copy h1 span{display:block;color:var(--gold)}
.hero-copy p{margin-top:8px;font-size:13px;font-weight:700;line-height:1.4}

.about{height:423px;position:relative}
.about h2{position:absolute;left:87px;top:117px;font-size:30px;font-weight:500}
.about p{position:absolute;left:87px;top:170px;width:580px;font-size:12.5px;line-height:2.05;color:var(--text-grey)}
.about-frame{position:absolute;left:717px;top:53px;width:396px;height:300px;border:8px solid var(--frame);border-left:none;border-bottom:none}
.about-photo{position:absolute;left:701px;top:58px;width:406px;height:313px;background:linear-gradient(120deg,#1d2a3a,#3d4c5e 55%,#8a8f94)}

.services{height:1096px;position:relative;background:linear-gradient(var(--orange) 0,var(--orange) 291px,var(--grey-bg) 291px)}
.services h2{position:absolute;top:48px;width:100%;text-align:center;color:var(--white);font-size:31px;font-weight:500}
.service-grid{position:absolute;left:87px;top:113px;display:grid;grid-template-columns:repeat(3,324px);column-gap:28px;row-gap:35px}
.service-card{height:410px;background:var(--white);box-shadow:0 2px 6px rgba(0,0,0,.15);text-align:center}
.service-photo{height:236px}
.service-card h3{margin-top:24px;font-size:14.5px;font-weight:700}
.service-card p{margin:8px auto 0;width:250px;font-size:12.5px;line-height:1.75;color:var(--text-grey)}
.btn{display:inline-block;background:var(--orange);color:var(--white);font-weight:700;font-size:13.5px;text-decoration:none;text-align:center}
.view-more{position:absolute;left:545px;top:1005px;width:110px;height:39px;line-height:39px}

.testimonial{height:356px;position:relative;background:linear-gradient(180deg,#1b1b1b,#2c2c2c 60%,#222);color:var(--white);text-align:center}
.testimonial h2{padding-top:44px;font-size:31px;font-weight:700}
.quote{position:relative;width:690px;margin:22px auto 0;font-size:13px;line-height:1.85}
.quote .mark{position:absolute;font-size:28px;font-weight:900;line-height:1}
.quote .open{left:-50px;top:-6px}
.quote .close{right:-50px;bottom:-10px}
.slider-arrow{position:absolute;top:156px}
.slider-arrow.prev{left:82px}
.slider-arrow.next{right:82px}
.avatar{width:58px;height:58px;border-radius:50%;margin:38px auto 0;background:linear-gradient(#c9b6a4,#8b7765);border:3px solid var(--white)}
.client-name{margin-top:8px;font-size:12.5px;font-weight:700}
.stars{margin-top:4px;display:flex;justify-content:center}

.contact{height:748px;position:relative}
.contact h2{position:absolute;top:50px;width:100%;text-align:center;font-size:31px;font-weight:500}
.contact-info{position:absolute;top:108px;width:100%;display:flex;flex-direction:column;align-items:center;gap:9px;font-size:12.5px;color:var(--text-grey)}
.contact-info .row{display:flex;align-items:center;gap:8px}
.contact-info .gap{margin-left:18px}
.contact-form{position:absolute;left:87px;top:186px;width:499px}
.contact-form label{display:block;font-size:12.5px;color:var(--text-grey);margin-bottom:8px}
.field{height:44px;border:1px solid var(--line);margin-bottom:20px}
.field.message{height:158px}
.send{position:absolute;left:388px;top:467px;width:111px;height:41px;line-height:41px}
.map{position:absolute;left:614px;top:191px;width:501px;height:503px;background:linear-gradient(135deg,#e4e6e3,#d9dde0 60%,#cfd9cc);border:1px solid var(--line)}

.site-footer{height:61px;background:var(--dark);color:var(--white);font-size:12.5px;text-align:center;line-height:61px}
</style>
</head>
<body>
<header class="site-header">
  <div class="brand"><span class="brand-mark"></span>K&amp;R Flame Guard Supply Inc.</div>
  <nav class="main-nav">
    <a class="active" href="#">HOME</a>
    <a href="#">ABOUT</a>
    <a href="#">OUR TRUCKS &amp; TEAMS</a>
    <a href="#">BOOK ONLINE</a>
    <a href="#">SERVICE AREAS</a>
  </nav>
</header>

<section class="hero">
  <div class="hero-photo" role="img" aria-label="Dim photo of fire sprinkler piping in a commercial ceiling"></div>
  <div class="hero-copy">
    <h1>DEDICATED TO<span>PROTECTING LIFE AND PROPERTY</span></h1>
    <p>Family owned and operated for over 30 years, we sell, service and install fire safety equipment for homes and businesses across all of Central Florida, from Tampa to Titusville. Restaurants, hotels, vacation rentals and small businesses trust us to keep them safe.</p>
  </div>
</section>

<section class="about">
  <h2>ABOUT US</h2>
  <p>K&amp;R Flame Guard Supply Inc. is a family owned and operated residential and commercial fire safety equipment company that has been in business for over 30 years. We provide sales, service and installation of fire extinguishers, emergency and exit lighting, kitchen fire suppression systems, fire alarms and fire extinguisher cabinets. Every business is required to have a fire extinguisher and exit lighting, and our team makes staying compliant simple. We proudly serve all of Central Florida, from Tampa to Titusville, with fast, friendly and professional service.</p>
  <div class="about-frame"></div>
  <div class="about-photo" role="img" aria-label="Technician inspecting a fire alarm control panel"></div>
</section>

<section class="services">
  <h2>OUR SERVICES</h2>
  <div class="service-grid">
    <article class="service-card"><div class="service-photo" role="img" aria-label="Row of red fire extinguishers" style="background:linear-gradient(160deg,#d8d2cc,#c8242a 55%,#7a1216)"></div><h3>Fire Extinguishers</h3><p>Sales of new fire extinguishers for every type of hazard, with the right size and rating chosen for your home, kitchen or business by our trained team.</p></article>
    <article class="service-card"><div class="service-photo" role="img" aria-label="Suppression system cylinders in a plant room" style="background:linear-gradient(180deg,#e9e6e3,#d7cfc9 45%,#c4262c)"></div><h3>Kitchen Fire Suppression</h3><p>Design, installation and inspection of kitchen hood suppression systems for restaurants and commercial kitchens, kept up to code year after year.</p></article>
    <article class="service-card"><div class="service-photo" role="img" aria-label="Wall mounted fire hose reel" style="background:linear-gradient(135deg,#e3dcd6,#c9444a 50%,#8e1e22)"></div><h3>Fire Alarms</h3><p>Installation, testing and service of fire alarm systems that give early warning and protect the people and property inside your building.</p></article>
    <article class="service-card"><div class="service-photo" role="img" aria-label="Hand gripping a fire extinguisher handle" style="background:linear-gradient(180deg,#e2e2e2,#c83236 60%,#9a1c20)"></div><h3>Extinguisher Service</h3><p>Annual inspections, recharging, hydrostatic testing and tagging of your fire extinguishers so they are always ready and fully compliant.</p></article>
    <article class="service-card"><div class="service-photo" role="img" aria-label="Sprinkler pipes under a white warehouse roof" style="background:linear-gradient(180deg,#f2f2f2,#cfd3d6)"></div><h3>Extinguisher Cabinets</h3><p>Supply and installation of surface and recessed fire extinguisher cabinets that keep equipment protected, visible and easy to reach.</p></article>
    <article class="service-card"><div class="service-photo" role="img" aria-label="Green emergency exit sign" style="background:linear-gradient(180deg,#c8cdc9,#1d9a4a 45%,#137a38 75%,#b5bab6)"></div><h3>Emergency &amp; Exit Lighting</h3><p>Sales, installation and testing of emergency and exit lighting that guides everyone safely out of your building when the power fails.</p></article>
  </div>
  <a class="btn view-more" href="#">VIEW MORE</a>
</section>

<section class="testimonial">
  <h2>TESTIMONIAL</h2>
  <div class="quote">
    <span class="mark open">&ldquo;</span>
    K&amp;R Flame Guard has handled the extinguishers, exit lighting and kitchen suppression system at our restaurant for years. They are always on time, explain everything clearly and keep us ready for every inspection. You can tell this family business truly cares.
    <span class="mark close">&rdquo;</span>
  </div>
  <svg class="slider-arrow prev" width="22" height="40" viewBox="0 0 22 40"><path d="M20 2 3 20l17 18" fill="none" stroke="#fff" stroke-width="2"/></svg>
  <svg class="slider-arrow next" width="22" height="40" viewBox="0 0 22 40"><path d="M2 2l17 18L2 38" fill="none" stroke="#fff" stroke-width="2"/></svg>
  <div class="avatar" role="img" aria-label="Client portrait"></div>
  <div class="client-name">DANA WHITFIELD</div>
  <div class="stars">
    <svg width="70" height="13" viewBox="0 0 70 13"><g fill="#f7c51a"><path id="star" d="M6.5 0l1.9 4.2 4.6.4-3.5 3 1.1 4.5-4.1-2.4-4.1 2.4 1.1-4.5-3.5-3 4.6-.4z"/><use href="#star" x="14"/><use href="#star" x="28"/><use href="#star" x="42"/><use href="#star" x="56"/></g></svg>
  </div>
</section>

<section class="contact">
  <h2>CONTACT US</h2>
  <div class="contact-info">
    <div class="row">
      <svg width="13" height="13" viewBox="0 0 24 24"><path fill="#f15a22" d="M6.6 10.8a15 15 0 0 0 6.6 6.6l2.2-2.2c.3-.3.7-.4 1-.2 1.1.4 2.3.6 3.6.6.6 0 1 .4 1 1V20c0 .6-.4 1-1 1A17 17 0 0 1 3 4c0-.6.4-1 1-1h3.5c.6 0 1 .4 1 1 0 1.3.2 2.5.6 3.6.1.3 0 .7-.2 1z"/></svg>
      <span>1-407-555-0142</span>
      <svg class="gap" width="14" height="11" viewBox="0 0 24 18"><path fill="#f15a22" d="M0 0h24v18H0zM2 2v.5l10 7 10-7V2z"/></svg>
      <span>krflameguard@example.com</span>
    </div>
    <div class="row">
      <svg width="11" height="15" viewBox="0 0 16 22"><path fill="#f15a22" d="M8 0a8 8 0 0 0-8 8c0 6 8 14 8 14s8-8 8-14a8 8 0 0 0-8-8zm0 11a3 3 0 1 1 0-6 3 3 0 0 1 0 6z"/></svg>
      <span>1450 Cypress Grove Rd, Lakeview, FL 34700</span>
    </div>
  </div>
  <form class="contact-form">
    <label>Name :</label><div class="field"></div>
    <label>Email Id :</label><div class="field"></div>
    <label>Phone Number :</label><div class="field"></div>
    <label>Message :</label><div class="field message"></div>
    <a class="btn send" href="#">SEND</a>
  </form>
  <div class="map" role="img" aria-label="Street map showing the company location"></div>
</section>

<footer class="site-footer">© 2018, K&amp;R Flame Guard Supply Inc. Serving Hillsborough, Polk, Osceola, Orange, Seminole &amp; Brevard counties. All Rights Reserved.</footer>
</body>
</html>
```